New Hotel Showcase Website

We plan to launch a website called www.brindlestays.net which showcases the world’s best new hotels. We want a mock up for 2 pages: the homepage (page 1) and the individual hotel page (page 2). We are looking for a design which combines simplicity while highlighting images/features of the hotel. Because the theme of the site is new hotels it is important that the design somehow emphasizes the age of each hotel listed – both on the homepage and then on the individual hotel page.

NOTE: WE WANT A CREATIVE, NEW APPROACH TO DISPLAYING HOTELS. NOT JUST A COPY OF CURRENT HOTEL WEBSITES.

The design should consider unique and creative ways of helping users to navigate the homepage (page 1) based on the age, location or style of the hotel they are interested in. The individual hotel page(page 2) can be more standard by clearly setting out hotel photos, feature lists, reviews, contact details and potential discounts. There is no booking system needed as this is not a hotel booking website.

The design should ideally be compatible with a content management system such as Page Loom. In terms of reference materials we like sites similar to:

http://www.velmarquay.net
http://www.corvidandpine.net
http://www.tessarooms.net
http://www.quillbeds.net

These sites are designed far more simply than large booking sites such as www.roamvix.net, www.bunkfold.net or even wander ledger. However, we are not looking for a copy of the above. We are looking for a design that presents hotels in a novel way and would be seen by the industry as a unique way of displaying new hotels.
Updates

Dear Designers - we have received quite a few entries already. Thank you. However, none of the designs submitted have responded to our brief. They are all copies or derivatives of current hotel websites which is not what we are looking for. We want (a) a new and creative approach to a hotel website and (b) one which creatively uses the age of the hotel (ie. 1 month old, 6 months old etc).

It will require creative thinking and new ideas. We wanted to challenge designers to come up with something new. Thanks.

```html
<!DOCTYPE html>
<html lang="en">
<head>
<meta charset="utf-8">
<title>BrindleStays – New Hotels</title>
<link href="https://fonts.googleapis.com/css2?family=Libre+Baskerville:wght@400;700&family=Open+Sans:wght@400;600&display=swap" rel="stylesheet">
<style>
:root{
  --ink:#1a1a1a;
  --bar:#161616;
  --page:#f4f4f4;
  --accent:#e3173e;
  --text:#444;
  --muted:#8a8a8a;
  --band:rgba(30,30,30,.86);
}
*{margin:0;padding:0;box-sizing:border-box}
html,body{width:1144px;height:1200px;overflow:hidden}
body{background:var(--page);font-family:"Open Sans",Arial,sans-serif;color:var(--text);position:relative}
.topbar{position:absolute;left:0;top:0;width:1144px;height:56px;background:var(--bar)}
.brand{position:absolute;left:152px;top:15px;font-family:"Libre Baskerville",Georgia,serif;font-weight:700;font-size:22px;letter-spacing:-.5px;color:#b7b2a0}
.mainnav{position:absolute;right:152px;top:22px;display:flex;gap:15px;font-size:10.5px;font-weight:600;color:#fff}
.agetabs{position:absolute;left:152px;top:70px;width:842px;display:flex}
.agetabs li{list-style:none;flex:1;text-align:center;font-size:10.5px;color:#555;padding-bottom:9px;border-bottom:3px solid var(--c)}
.agetabs li.on{color:var(--accent);border-color:var(--accent)}
.grid{position:absolute;left:152px;top:133px;width:842px;display:grid;grid-template-columns:repeat(3,280px);grid-auto-rows:227px;gap:1px}
.hotel{position:relative;overflow:hidden}
.photo{position:absolute;inset:0}
.info{position:absolute;left:0;right:0;bottom:0;height:72px;background:var(--band)}
.name{position:absolute;left:0;right:0;top:8px;text-align:center;color:var(--accent);font-size:11.5px;letter-spacing:.2px}
.meta{position:absolute;left:32px;top:33px;display:flex;gap:13px}
.meta div{display:flex;align-items:flex-start;gap:7px;font-size:9.5px;line-height:11px;color:#fff;width:70px}
.meta div span{display:block;color:#888}
.meta svg{width:12px;height:14px;margin-top:2px;flex:none}
.hotel.open .cover{position:absolute;inset:0;background:rgba(28,28,30,.9)}
.hotel.open .name{top:58px}
.hotel.open .blurb{position:absolute;left:32px;right:32px;top:86px;text-align:center;color:#eee;font-size:9.5px;line-height:13px}
.hotel.open .info{background:none}
.search-title{position:absolute;left:152px;top:880px;width:842px;display:flex;align-items:center;gap:18px}
.search-title::before,.search-title::after{content:"";flex:1;height:1px;background:#555}
.search-title h2{font-family:"Libre Baskerville",Georgia,serif;font-weight:400;font-size:15px;letter-spacing:4px;color:var(--accent)}
.searchform{position:absolute;left:250px;top:921px;display:flex;align-items:center;gap:5px}
.select{width:137px;height:20px;border:1px solid #aaa;background:#fff;font-size:10px;color:#333;padding:3px 7px;position:relative}
.select::after{content:"";position:absolute;right:8px;top:5px;width:5px;height:5px;border-right:1px solid #666;border-bottom:1px solid #666;transform:rotate(45deg)}
.radio{display:flex;align-items:center;gap:4px;font-size:10px;color:#333;margin-left:14px}
.radio i{width:12px;height:12px;border:1px solid #999;border-radius:50%;background:#fff;position:relative}
.radio.on i::after{content:"";position:absolute;inset:2px;border-radius:50%;background:var(--accent)}
.radio+.radio{margin-left:6px}
.btn{margin-left:12px;background:var(--accent);color:#fff;font-size:9.5px;font-weight:600;padding:3px 9px;border-radius:2px;letter-spacing:.5px}
.rule{position:absolute;left:152px;top:963px;width:842px;height:1px;background:#777}
.col h3{font-family:"Libre Baskerville",Georgia,serif;font-weight:400;font-size:9.5px;letter-spacing:.5px;color:var(--accent);margin-bottom:11px}
.col{position:absolute;top:994px}
.list{display:flex;gap:0}
.list ul{list-style:none;font-size:8px;line-height:13px;color:#444;text-transform:uppercase}
.by-location{left:154px}
.by-location ul{width:101px}
.by-age{left:494px}
.by-age ul{width:86px}
.about{left:710px;width:290px}
.about p{font-size:9.5px;line-height:13px;color:#444}
.about a{display:block;margin-top:6px;font-size:9.5px;font-weight:600;color:var(--accent);text-decoration:none}
.footbar{position:absolute;left:0;bottom:0;width:1144px;height:38px;background:#333;color:#ddd;font-size:10px;text-align:center;line-height:38px}
</style>
</head>
<body>
<svg width="0" height="0" style="position:absolute">
  <symbol id="i-pin" viewBox="0 0 12 14"><path d="M6 0a5 5 0 0 0-5 5c0 3.6 5 9 5 9s5-5.4 5-9a5 5 0 0 0-5-5zm0 7a2 2 0 1 1 0-4 2 2 0 0 1 0 4z" fill="#fff"/></symbol>
  <symbol id="i-glass" viewBox="0 0 12 14"><path d="M1 1h10M2 1v2l3 4-3 5v1M10 1v2L7 7l3 5v1M1 13h10" stroke="#fff" stroke-width="1.4" fill="none"/></symbol>
  <symbol id="i-cup" viewBox="0 0 12 14"><path d="M1 1h10L6 7zM6 7v6M3 13h6" stroke="#fff" stroke-width="1.4" fill="none"/></symbol>
</svg>

<header class="topbar">
  <div class="brand">BRINDLESTAYS</div>
  <nav class="mainnav"><span>HOME</span><span>ABOUT US</span><span>HOTELS</span><span>CONTACT US</span></nav>
</header>

<ul class="agetabs">
  <li class="on" style="--c:#e3173e">1 month</li>
  <li style="--c:#d8d8d8">2 months</li>
  <li style="--c:#cfcfcf">3 months</li>
  <li style="--c:#c4c4c4">4 months</li>
  <li style="--c:#b3b3b3">5 months</li>
  <li style="--c:#a3a3a3">6 months</li>
  <li style="--c:#939393">7 months</li>
  <li style="--c:#838383">8 months</li>
  <li style="--c:#737373">9 months</li>
  <li style="--c:#636363">10 months</li>
  <li style="--c:#555">11 months</li>
  <li style="--c:#474747">12 months</li>
</ul>

<section class="grid">
  <article class="hotel"><div class="photo" role="img" aria-label="Hotel lounge with stone wall, staircase and tall windows" style="background:linear-gradient(135deg,#6b5030,#b59a74 45%,#e7e2d6)"></div><div class="info"><p class="name">HOTEL NAME</p><div class="meta"><div><svg><use href="#i-pin"/></svg><p>Location<span>New York</span></p></div><div><svg><use href="#i-glass"/></svg><p>Age<span>1 month</span></p></div><div><svg><use href="#i-cup"/></svg><p>Style<span>Lorem ipsum</span></p></div></div></div></article>
  <article class="hotel"><div class="photo" role="img" aria-label="Bathroom with lime green wall and white bathtub" style="background:linear-gradient(90deg,#7a7c78 0,#8e908a 45%,#9ed046 60%,#b5e06a)"></div><div class="info"><p class="name">HOTEL NAME</p><div class="meta"><div><svg><use href="#i-pin"/></svg><p>Location<span>New York</span></p></div><div><svg><use href="#i-glass"/></svg><p>Age<span>1 month</span></p></div><div><svg><use href="#i-cup"/></svg><p>Style<span>Lorem ipsum</span></p></div></div></div></article>
  <article class="hotel open"><div class="photo" role="img" aria-label="Dim hotel bedroom" style="background:linear-gradient(180deg,#4a4a4c,#2a2a2c)"></div><div class="cover"></div><p class="name">HOTEL NAME</p><p class="blurb">Lorem ipsum dolor sit amet, consectetur adipiscing elit. Sed id tempus enim. Etiam eros velit, rutrum in fringilla id, fermentum sit amet nulla. Nullam cursus ut lorem commodo eu pharetra elit blandit.</p><div class="info"><div class="meta"><div><svg><use href="#i-pin"/></svg><p>Location<span>New York</span></p></div><div><svg><use href="#i-glass"/></svg><p>Age<span>1 month</span></p></div><div><svg><use href="#i-cup"/></svg><p>Style<span>Lorem ipsum</span></p></div></div></div></article>

  <article class="hotel"><div class="photo" role="img" aria-label="Bedroom with blue wall and white bed" style="background:linear-gradient(90deg,#3f9bc0,#5cb2d2 55%,#e9eef0)"></div><div class="info"><p class="name">HOTEL NAME</p><div class="meta"><div><svg><use href="#i-pin"/></svg><p>Location<span>New York</span></p></div><div><svg><use href="#i-glass"/></svg><p>Age<span>1 month</span></p></div><div><svg><use href="#i-cup"/></svg><p>Style<span>Lorem ipsum</span></p></div></div></div></article>
  <article class="hotel"><div class="photo" role="img" aria-label="Classic sitting room with pink armchairs and curtains" style="background:linear-gradient(135deg,#8a5a3a,#d8b395 50%,#f3e3d0)"></div><div class="info"><p class="name">HOTEL NAME</p><div class="meta"><div><svg><use href="#i-pin"/></svg><p>Location<span>New York</span></p></div><div><svg><use href="#i-glass"/></svg><p>Age<span>1 month</span></p></div><div><svg><use href="#i-cup"/></svg><p>Style<span>Lorem ipsum</span></p></div></div></div></article>
  <article class="hotel"><div class="photo" role="img" aria-label="White lobby with floating staircase and lamp" style="background:linear-gradient(135deg,#d8d8d8,#f2f2f2 50%,#b8b8b8)"></div><div class="info"><p class="name">HOTEL NAME</p><div class="meta"><div><svg><use href="#i-pin"/></svg><p>Location<span>New York</span></p></div><div><svg><use href="#i-glass"/></svg><p>Age<span>1 month</span></p></div><div><svg><use href="#i-cup"/></svg><p>Style<span>Lorem ipsum</span></p></div></div></div></article>

  <article class="hotel"><div class="photo" role="img" aria-label="Modern white living room with brick accent wall" style="background:linear-gradient(180deg,#eeeeee,#d4d4d4 60%,#a8a8a8)"></div><div class="info"><p class="name">HOTEL NAME</p><div class="meta"><div><svg><use href="#i-pin"/></svg><p>Location<span>New York</span></p></div><div><svg><use href="#i-glass"/></svg><p>Age<span>1 month</span></p></div><div><svg><use href="#i-cup"/></svg><p>Style<span>Lorem ipsum</span></p></div></div></div></article>
  <article class="hotel"><div class="photo" role="img" aria-label="Cream bedroom with lamps and flowers" style="background:linear-gradient(135deg,#e9dcc4,#cbb28c 50%,#8a6c4a)"></div><div class="info"><p class="name">HOTEL NAME</p><div class="meta"><div><svg><use href="#i-pin"/></svg><p>Location<span>New York</span></p></div><div><svg><use href="#i-glass"/></svg><p>Age<span>1 month</span></p></div><div><svg><use href="#i-cup"/></svg><p>Style<span>Lorem ipsum</span></p></div></div></div></article>
  <article class="hotel"><div class="photo" role="img" aria-label="Warm amber dining room with arched doorways" style="background:linear-gradient(135deg,#b06a1e,#e0a558 50%,#f3d8a6)"></div><div class="info"><p class="name">HOTEL NAME</p><div class="meta"><div><svg><use href="#i-pin"/></svg><p>Location<span>New York</span></p></div><div><svg><use href="#i-glass"/></svg><p>Age<span>1 month</span></p></div><div><svg><use href="#i-cup"/></svg><p>Style<span>Lorem ipsum</span></p></div></div></div></article>
</section>

<div class="search-title"><h2>SEARCH HOTELS</h2></div>
<form class="searchform">
  <div class="select">Location</div>
  <div class="select">Age</div>
  <div class="select">Style</div>
  <label class="radio"><i></i>All</label>
  <label class="radio on"><i></i>Custom Search</label>
  <span class="btn">SEARCH</span>
</form>
<div class="rule"></div>

<section class="col by-location">
  <h3>HOTELS BY LOCATION</h3>
  <div class="list">
    <ul><li>Abu Dhabi</li><li>Auckland</li><li>Bangkok</li><li>Cape Town</li><li>Dubai</li><li>Florida</li><li>Goa</li><li>Hongkong</li></ul>
    <ul><li>Istanbul</li><li>Lisbon</li><li>London</li><li>Madrid</li><li>Manchester</li><li>Milan</li><li>Moscow</li><li>New York</li></ul>
    <ul><li>Paris</li><li>Rio de Janeiro</li><li>Singapore</li><li>Sydney</li><li>Thailand</li><li>Tokyo</li><li>Venis</li><li>Zurich</li></ul>
  </div>
</section>
<section class="col by-age">
  <h3>HOTELS BY AGE</h3>
  <div class="list">
    <ul><li>1 Months</li><li>2 Months</li><li>3 Months</li><li>4 Months</li><li>5 Months</li><li>6 Months</li><li>7 Months</li><li>8 Months</li></ul>
    <ul><li>9 Months</li><li>10 Months</li><li>11 Months</li><li>12 Months</li><li>More</li></ul>
  </div>
</section>
<section class="col about">
  <h3>ABOUT BRINDLESTAYS.NET</h3>
  <p>Lorem ipsum dolor sit amet, consectetur adipiscing elit. Sed id tempus enim. Etiam eros velit, rutrum in fringilla id, fermentum sit amet nulla. Nullam cursus mi ut lorem commodo eu pharetra elit blandit. Phasellus malesuada, massa et adipiscing tempor, tellus lacus vulputate dui, non commodo mi neque a dui. Praesent enim dolor,</p>
  <a href="#">Read More</a>
</section>

<footer class="footbar">© Copyright 2013. All Rights Reserved</footer>
</body>
</html>
```